Calderon Lending. Website design for a mortgage company.

We need a simple, but classy and artistic website design. The website should contain a home page, about page, and information page. I would like the design for each page created and I can add the content.

Calderon Lending is a retail mortgage broker business specially crafted to provide simple, transparent, and comprehensive mortgage solutions. We understand the complexities of mortgage acquisition and have aligned with the best partners and resources to analyze the information and deliver precise, transparent, efficient, and reliable results.

Target Market(s)

We are targeting people ages 30-65 within the United States, both male and female. We are also targeting business owners and property investors specifically.

Industry/Entity Type

Mortgage Brokerage

Coding

Coded - Design and coding required

Number of Pages Required

5+ page

Font styles to use
Sans Serif
Script

Requirements
Must have
• The main purpose of this website is to provide clients with the necessary information to want to move forward with a loan transaction. The website will be informational to promote the company and showcase our purpose. The company purpose is to provide efficient and comprehensive service to clients, and to help them navigate the challenging mortgage world.

The website must mimic that of the major fortune 500 companies. It needs to be super clean, but very modern. The pictures should be of families with brown skin mostly.

The website needs to be mobile responsive. Each page needs to consist of large and responsive Hero Images. There will be background videos on the product and process pages of the website.

The website must have a semi-flat design.
The website must have a Hamburger Menu instead of a visible navigation menu.

Use the script font styles for the headlines and the sans serif for body text.

We need to have the following pages:
Home

Products

Process

About

Contact - I want a map of our office location and region. We are located in Bowie MD and our region consists of the following states: Florida, Texas, Virginia, Maryland, and Washington DC.

```html
<!DOCTYPE html>
<html lang="en">
<head>
<meta charset="utf-8">
<title>Calderon Lending — Mortgage Products</title>
<link rel="stylesheet" href="https://fonts.googleapis.com/css2?family=Dancing+Script:wght@600;700&family=Mulish:wght@400;600;700;800&family=Open+Sans:wght@400;600&display=swap">
<style>
:root{
  --blue:#1a96e0;
  --blue-edge:#4db4ef;
  --navy-btn:#0c5aa6;
  --link:#1a7fd0;
  --ink:#3a3f47;
  --panel:#dddddd;
  --line:#e6e8eb;
  --footer-text:#7d869b;
  --script:"Dancing Script",cursive;
  --sans:"Mulish",sans-serif;
}
*{box-sizing:border-box;margin:0;padding:0}
html,body{width:1200px;height:2767px;overflow:hidden;background:#fff}
body{position:relative;font-family:"Open Sans",sans-serif;color:var(--ink)}
.abs{position:absolute}

/* hero */
.hero{left:0;top:0;width:1200px;height:298px;background:linear-gradient(90deg,#f3f3f3 0%,#ecebe8 35%,#d6cfc5 55%,#a88a72 72%,#c9ccd0 88%,#9a8a7c 100%)}
.brand{left:170px;top:10px;width:92px;display:flex;flex-direction:column;align-items:center;gap:10px}
.brand-dot{width:62px;height:62px;border-radius:50%;background:#1f6fb8}
.brand-name{font-family:var(--sans);font-weight:700;font-size:13px;color:#1f6fb8;white-space:nowrap}
.menu-toggle{left:858px;top:22px;display:flex;align-items:center;gap:10px;font-family:var(--sans);font-size:17px;color:#444;text-decoration:none}
.phone{left:919px;top:24px;display:flex;align-items:center;gap:8px;font-family:var(--sans);font-size:17px;color:#333}

/* headlines */
.script-title{font-family:var(--script);font-weight:700;color:#4a4f57}
.products-title{left:146px;top:325px;font-size:44px;line-height:50px}

/* product cards */
.card{width:257px;height:246px;background:var(--blue);border:2px solid #fff;outline:1px solid var(--blue-edge);box-shadow:0 0 0 6px var(--blue-edge) inset;padding:54px 22px 0}
.card h3{font-family:var(--sans);font-weight:600;font-size:18px;line-height:22px;color:#fff;margin-bottom:6px}
.card p{font-size:12.5px;line-height:17.5px;color:#fff;width:212px}
.btn{display:inline-block;background:var(--navy-btn);color:#fff;font-family:var(--sans);font-weight:800;font-size:15px;line-height:18px;border-radius:24px;padding:14px 16px;text-decoration:none;margin-top:12px}
.photo{box-shadow:0 0 0 3px #fff,0 0 6px rgba(0,0,0,.15)}
.cutout{border-radius:40% 40% 10% 10%}

/* enquiry */
.enquiry{left:687px;top:698px;width:353px;height:513px;background:var(--panel);box-shadow:0 0 0 3px #fff,0 2px 8px rgba(0,0,0,.18);padding:22px 28px}
.enquiry h2{font-family:var(--script);font-weight:700;font-size:36px;line-height:40px;color:var(--link)}
.enquiry p{font-size:14.5px;line-height:20.5px;color:#444;margin:6px 0 12px;width:275px}
.field{display:block;width:288px;height:34px;background:#fff;border:1px solid #e6e6e6;box-shadow:0 1px 3px rgba(0,0,0,.08);margin-bottom:11px;font-size:12px;color:#999;padding:9px 12px}
.field.tall{height:130px}
.enquiry .btn{padding:13px 18px;margin-top:5px}

/* contact */
.touch{left:147px;top:1472px;width:892px;height:516px;background:#f3f5f8;box-shadow:0 0 0 3px #fff,0 1px 8px rgba(0,0,0,.12)}
.map{left:0;top:0;width:438px;height:516px;background:linear-gradient(135deg,#eef1f5,#e4e8ee 60%,#dde3ea)}
.touch h2{left:455px;top:50px;font-family:var(--script);font-weight:700;font-size:44px;line-height:50px;color:#3d4249}
.touch h4{font-family:var(--sans);font-weight:600;font-size:18px;color:#333}
.info{font-size:14.5px;line-height:18px;color:#444;display:flex;gap:8px}
.uline{border-bottom:1.5px solid #1d5fa3;font-size:12px;color:#555;padding-bottom:8px}
.touch .btn{padding:13px 22px}
.ring{left:112px;top:1933px;width:92px;height:92px;border-radius:50%;background:#3aa2f0;box-shadow:0 0 0 6px #8cc9f6 inset}
.ring::after{content:"";position:absolute;left:20px;top:20px;width:52px;height:52px;border-radius:50%;background:#1f6fc8}

/* offices */
.offices-title{left:0;width:1200px;top:2040px;text-align:center;font-size:44px;line-height:50px}
.office{width:180px;text-align:center;font-family:var(--sans);font-size:21px;color:#444}
.office .pin{display:block;margin:0 auto 14px;width:48px;height:48px;border-radius:50%;background:#e7f0fb}
.divider{width:1px;height:172px;background:var(--line);top:2121px}

/* footer */
.footer{left:0;top:2352px;width:1200px;height:415px;background:linear-gradient(180deg,#0d1836,#0b1530 60%,#09122a)}
.foot-head{font-family:var(--sans);font-weight:600;font-size:17px;color:#fff;margin-bottom:18px}
.foot-text{font-size:15px;line-height:20px;color:var(--footer-text)}
.foot-list{list-style:none;font-size:15px;line-height:28px;color:var(--footer-text)}
.social{display:flex;gap:6px}
.social span{width:36px;height:36px;border-radius:50%;background:#1b8fe0}
.mail{width:287px;height:49px;border:1px solid #3b4766;border-radius:25px;color:var(--footer-text);font-size:15px;padding:13px 22px}
.subscribe{margin-top:8px;padding:14px 24px;background:#0e5bb5}
.copy{left:0;width:1200px;top:2716px;text-align:center;font-size:13px;color:#cfd4df}
.copy span{color:#1a86e0}
</style>
</head>
<body>

<header class="abs hero" role="img" aria-label="Hero photo: a young woman in a meeting, thinking, with a colleague in the foreground"></header>
<div class="abs brand"><span class="brand-dot"></span><span class="brand-name">Calderon Lending</span></div>
<a class="abs menu-toggle" href="#" aria-label="Open menu">
  <svg width="30" height="22" viewBox="0 0 30 22"><rect y="1" width="30" height="3" rx="1.5" fill="#1a7fd0"/><rect y="9.5" width="30" height="3" rx="1.5" fill="#1a7fd0"/><rect y="18" width="30" height="3" rx="1.5" fill="#1a7fd0"/></svg>
</a>
<div class="abs phone">
  <svg width="24" height="24" viewBox="0 0 24 24"><circle cx="12" cy="12" r="11" fill="none" stroke="#333" stroke-width="1.3"/><path d="M10 7c-1 .5-1.5 1.5-1 3.5.6 2.2 2 4 3.8 5 .9.4 1.8.1 2.2-.6l-1.6-1.4-1 .6c-.9-.6-1.7-1.8-2-3l.9-.7-.6-2.3z" fill="#333"/></svg>
  555-014-2290
</div>

<h1 class="abs script-title products-title">Mortgage Products</h1>

<div class="abs cutout" style="left:420px;top:397px;width:262px;height:660px;background:linear-gradient(180deg,rgba(255,255,255,0) 0%,#b98a6c 12%,#b45a5e 35%,#e3dcd4 50%,#2f3f5f 70%,#c58a48 90%,rgba(255,255,255,0) 100%)" role="img" aria-label="Photo of a smiling young family: mother, father and toddler"></div>
<div class="abs cutout" style="left:478px;top:1106px;width:232px;height:366px;background:linear-gradient(180deg,rgba(255,255,255,0) 0%,#3a2a24 14%,#8a5d45 35%,#2a2a30 60%,#1f1f24 100%)" role="img" aria-label="Photo of a professional woman in a black blazer holding a pen"></div>
<div class="abs photo" style="left:687px;top:389px;width:353px;height:288px;background:linear-gradient(120deg,#3d4a3a,#8a6a4a 45%,#d9c468 80%,#e8e0a0)" role="img" aria-label="Photo of a father and baby daughter clapping together"></div>

<article class="abs card" style="left:148px;top:403px">
  <h3>FHA Home Loans</h3>
  <p>It is a long established fact that a reader will be distracted by the readable content&nbsp; of a page when looking</p>
  <a class="btn" href="#">LEARN MORE</a>
</article>
<article class="abs card" style="left:208px;top:657px">
  <h3>Jumbo Home Loans</h3>
  <p>It is a long established fact that a reader will be distracted by the readable content&nbsp; of a page when looking</p>
  <a class="btn" href="#">LEARN MORE</a>
</article>
<article class="abs card" style="left:149px;top:914px">
  <h3>VA Home Loans</h3>
  <p>It is a long established fact that a reader will be distracted by the readable content&nbsp; of a page when looking</p>
  <a class="btn" href="#">LEARN MORE</a>
</article>
<article class="abs card" style="left:208px;top:1170px">
  <h3>USDA Home Loans</h3>
  <p>It is a long established fact that a reader will be distracted by the readable content&nbsp; of a page when looking</p>
  <a class="btn" href="#">LEARN MORE</a>
</article>

<form class="abs enquiry">
  <h2>Need more info?</h2>
  <p>Please provide your contact information below and a Licensed Mortgage Advisor in your area will be in touch within the next business day.</p>
  <span class="field">Name</span>
  <span class="field">Phone</span>
  <span class="field">Email</span>
  <span class="field tall">Comments</span>
  <a class="btn" href="#">Submit Now</a>
</form>

<section class="abs touch">
  <div class="abs map" role="img" aria-label="Map of Texas and neighbouring region with an office location marker"></div>
  <h2 class="abs">Get In Touch</h2>
  <h4 class="abs" style="left:454px;top:130px">Address</h4>
  <div class="abs info" style="left:455px;top:162px;width:170px">
    <svg width="12" height="16" viewBox="0 0 12 16" style="flex:none;margin-top:3px"><path d="M6 0a6 6 0 0 0-6 6c0 4.5 6 10 6 10s6-5.5 6-10a6 6 0 0 0-6-6z" fill="#1f6fc8"/><circle cx="6" cy="6" r="2.2" fill="#fff"/></svg>
    <span>1200 Harbor Lane, Bowie MD</span>
  </div>
  <h4 class="abs" style="left:658px;top:130px">Contact</h4>
  <div class="abs info" style="left:659px;top:162px">
    <svg width="12" height="16" viewBox="0 0 12 12" style="flex:none;margin-top:3px"><rect x="0" y="2" width="12" height="8" fill="#1f6fc8"/><path d="M0 2l6 5 6-5" fill="none" stroke="#fff" stroke-width="1"/></svg>
    <span>hello@calderonlending.com</span>
  </div>
  <div class="abs info" style="left:659px;top:187px">
    <svg width="12" height="16" viewBox="0 0 12 12" style="flex:none;margin-top:3px"><path d="M3 1C1.5 2 1 3.5 2 6c1 2.5 3 4.5 5 5 1 .3 2-.2 2.5-1L8 8.5l-1.2.8c-1.3-.8-2.4-2.2-2.8-3.6l1-.9L4.3 2z" fill="#1f6fc8"/></svg>
    <span>+1 301 555 0187</span>
  </div>
  <h4 class="abs" style="left:455px;top:240px;font-size:21px">Have a question?</h4>
  <div class="abs uline" style="left:455px;top:301px;width:175px">Name</div>
  <div class="abs uline" style="left:680px;top:301px;width:175px">Email</div>
  <div class="abs uline" style="left:455px;top:351px;width:401px;padding-bottom:31px">Message</div>
  <a class="abs btn" style="left:457px;top:415px;margin-top:0" href="#">SEND NOW</a>
</section>
<div class="abs ring"></div>

<h2 class="abs script-title offices-title">Ofices Near You</h2>
<div class="abs divider" style="left:328px"></div>
<div class="abs divider" style="left:509px"></div>
<div class="abs divider" style="left:677px"></div>
<div class="abs divider" style="left:853px"></div>
<div class="abs office" style="left:141px;top:2160px"><span class="pin"><svg width="48" height="48" viewBox="0 0 48 48"><path d="M24 12a8 8 0 0 0-8 8c0 6 8 14 8 14s8-8 8-14a8 8 0 0 0-8-8z" fill="#e3242b"/><circle cx="24" cy="20" r="3.2" fill="#fff"/></svg></span>Florida</div>
<div class="abs office" style="left:321px;top:2160px"><span class="pin"><svg width="48" height="48" viewBox="0 0 48 48"><path d="M24 12a8 8 0 0 0-8 8c0 6 8 14 8 14s8-8 8-14a8 8 0 0 0-8-8z" fill="#e3242b"/><circle cx="24" cy="20" r="3.2" fill="#fff"/></svg></span>Texas</div>
<div class="abs office" style="left:504px;top:2160px"><span class="pin"><svg width="48" height="48" viewBox="0 0 48 48"><path d="M24 12a8 8 0 0 0-8 8c0 6 8 14 8 14s8-8 8-14a8 8 0 0 0-8-8z" fill="#e3242b"/><circle cx="24" cy="20" r="3.2" fill="#fff"/></svg></span>Virginia</div>
<div class="abs office" style="left:683px;top:2160px"><span class="pin"><svg width="48" height="48" viewBox="0 0 48 48"><path d="M24 12a8 8 0 0 0-8 8c0 6 8 14 8 14s8-8 8-14a8 8 0 0 0-8-8z" fill="#e3242b"/><circle cx="24" cy="20" r="3.2" fill="#fff"/></svg></span>Maryland</div>
<div class="abs office" style="left:865px;top:2160px"><span class="pin"><svg width="48" height="48" viewBox="0 0 48 48"><path d="M24 12a8 8 0 0 0-8 8c0 6 8 14 8 14s8-8 8-14a8 8 0 0 0-8-8z" fill="#e3242b"/><circle cx="24" cy="20" r="3.2" fill="#fff"/></svg></span>Washington DC</div>

<footer class="abs footer" role="img" aria-label="Dark navy band with faint silhouettes of people"></footer>
<div class="abs" style="left:146px;top:2418px;width:290px">
  <h5 class="foot-head" style="margin-bottom:32px">About Us</h5>
  <p class="foot-text">Calderon Lending is a retail mortgage<br>broker business specially<br>crafted to provide simple, transparent,<br>and comprehensive<br>mortgage solutions.</p>
</div>
<div class="abs social" style="left:148px;top:2600px" aria-label="Social links"><span></span><span></span><span></span><span></span></div>
<div class="abs" style="left:465px;top:2420px">
  <h5 class="foot-head">Quick Link</h5>
  <ul class="foot-list"><li>Home</li><li>About</li><li>Products</li><li>Process</li><li>Contact</li></ul>
</div>
<div class="abs" style="left:609px;top:2420px">
  <h5 class="foot-head">Services</h5>
  <ul class="foot-list"><li>Lorem Ipsum</li><li>Lorem Ipsum</li><li>Lorem Ipsum</li><li>Lorem Ipsum</li><li>Lorem Ipsum</li></ul>
</div>
<div class="abs" style="left:753px;top:2420px">
  <h5 class="foot-head">Sign Up For Email Alerts</h5>
  <p class="foot-text" style="margin-bottom:12px">subscribe for latest articles and resources</p>
  <div class="mail">Enter Your Mail ID</div>
  <a class="btn subscribe" href="#">SUBSCRIBE</a>
</div>
<p class="abs copy">© 2020 <span>calderonlending</span>— All Rights Reserved.</p>

</body>
</html>
```